Business Card Design for The Lending Nook Inc.

We need a business card design for our mortgage company: "The Lending Nook Inc."

Need to have Social Media Account on there as a possibility

Industry/Entity Type

Business

```html
<!DOCTYPE html>
<html lang="en">
<head>
<meta charset="utf-8">
<title>The Lending Nook Inc. – Business Card</title>
<link href="https://fonts.googleapis.com/css2?family=Open+Sans:wght@400;600;700&display=swap" rel="stylesheet">
<style>
  :root {
    --brand-blue: #0f5aa8;
    --brand-blue-deep: #0b4f97;
    --ink-dark: #3a3f47;
    --ink-soft: #5b616b;
    --paper: #ffffff;
    --backdrop: #e9ebee;
    --faint-mark: rgba(0, 0, 0, 0.06);
    --faint-mark-light: rgba(255, 255, 255, 0.16);
  }
  * { box-sizing: border-box; margin: 0; padding: 0; }
  html, body {
    width: 1200px; height: 834px; overflow: hidden;
    background: var(--backdrop);
    font-family: "Open Sans", Arial, sans-serif;
  }
  .canvas {
    width: 1200px; height: 834px;
    display: flex; align-items: center; justify-content: center; gap: 40px;
  }
  .card {
    position: relative; width: 540px; height: 309px; overflow: hidden;
    box-shadow: 0 6px 18px rgba(0,0,0,0.18);
  }
  .card--back { background: var(--brand-blue-deep); color: var(--paper); }
  .card--front { background: var(--paper); color: var(--ink-dark); }

  .decor-ring {
    position: absolute; border-radius: 50%;
  }
  .card--back .decor-ring {
    width: 300px; height: 300px; right: -40px; bottom: -120px;
    border: 16px solid var(--faint-mark-light);
  }
  .card--front .decor-ring {
    width: 240px; height: 240px; right: -50px; bottom: -110px;
    border: 14px solid var(--faint-mark);
  }

  .brand { display: flex; align-items: center; gap: 12px; }
  .brand-dot { border-radius: 50%; flex: none; }
  .brand-name { font-weight: 600; letter-spacing: 0.2px; }

  .card--back .brand {
    position: absolute; left: 70px; top: 92px;
  }
  .card--back .brand-dot { width: 52px; height: 52px; border: 3px solid var(--paper); }
  .card--back .brand-name { font-size: 30px; color: var(--paper); }
  .card--back .brand-rule {
    position: absolute; left: 134px; top: 150px; width: 330px; height: 1.5px;
    background: var(--paper);
  }
  .website {
    position: absolute; left: 40px; bottom: 34px;
    font-size: 15px; letter-spacing: 0.6px; opacity: 0.85;
  }

  .card--front .brand { position: absolute; left: 28px; top: 40px; }
  .card--front .brand-dot { width: 30px; height: 30px; border: 2px solid var(--brand-blue); }
  .card--front .brand-name { font-size: 18px; color: var(--brand-blue); }
  .divider {
    position: absolute; left: 272px; top: 120px; width: 1.5px; height: 100px;
    background: var(--brand-blue);
  }
  .contact { position: absolute; left: 292px; top: 110px; }
  .person-name { font-size: 21px; font-weight: 700; color: var(--brand-blue); line-height: 1.1; }
  .person-title { font-size: 10px; color: var(--ink-soft); margin-bottom: 12px; }
  .contact-list { list-style: none; }
  .contact-item {
    display: flex; align-items: flex-start; gap: 8px;
    font-size: 11px; color: var(--ink-dark); margin-bottom: 8px; line-height: 1.35;
  }
  .contact-item--email { font-weight: 600; }
  .contact-icon { width: 14px; height: 14px; flex: none; margin-top: 1px; }
</style>
</head>
<body>
<main class="canvas">
  <section class="card card--back" aria-label="Business card back">
    <div class="decor-ring"></div>
    <div class="brand">
      <span class="brand-dot"></span>
      <span class="brand-name">The Lending Nook Inc.</span>
    </div>
    <div class="brand-rule"></div>
    <p class="website">www.lendingnook.com</p>
  </section>

  <section class="card card--front" aria-label="Business card front">
    <div class="decor-ring"></div>
    <div class="brand">
      <span class="brand-dot"></span>
      <span class="brand-name">The Lending Nook Inc.</span>
    </div>
    <div class="divider"></div>
    <div class="contact">
      <h1 class="person-name">Mr. Daniel Reyes</h1>
      <p class="person-title">General Director</p>
      <ul class="contact-list">
        <li class="contact-item">
          <svg class="contact-icon" viewBox="0 0 14 14" aria-hidden="true">
            <rect x="1" y="1" width="12" height="12" rx="3" fill="none" stroke="#0f5aa8" stroke-width="1.2"/>
            <rect x="5" y="3.5" width="4" height="7" rx="0.8" fill="none" stroke="#0f5aa8" stroke-width="1"/>
          </svg>
          <span>+1 555 0142</span>
        </li>
        <li class="contact-item contact-item--email">
          <svg class="contact-icon" viewBox="0 0 14 14" aria-hidden="true">
            <rect x="1" y="1" width="12" height="12" rx="3" fill="none" stroke="#0f5aa8" stroke-width="1.2"/>
            <path d="M3.5 4.5h7v5h-7z M3.5 4.5l3.5 3 3.5-3" fill="none" stroke="#0f5aa8" stroke-width="1"/>
          </svg>
          <span>hello@lendingnook.com</span>
        </li>
        <li class="contact-item">
          <svg class="contact-icon" viewBox="0 0 14 14" aria-hidden="true">
            <circle cx="7" cy="7" r="6.2" fill="#0f5aa8"/>
            <path d="M7 3.2a2.4 2.4 0 0 1 2.4 2.4C9.4 7.4 7 10.6 7 10.6S4.6 7.4 4.6 5.6A2.4 2.4 0 0 1 7 3.2z" fill="#fff"/>
            <circle cx="7" cy="5.6" r="0.9" fill="#0f5aa8"/>
          </svg>
          <span>Maple Row Av. 48<br>40215, North Bristol</span>
        </li>
      </ul>
    </div>
  </section>
</main>
</body>
</html>
```